Springtime Saver Special Promotional Postcard

I would like a postcard designed for a credit card balance transfer promotion.

The title for this promotion is "Springtime saver special".

(This paragraph should not be used word for word) Credit Card rates are on the rise since the Federal Prime Rate increase. I want to promote a non-variable rate credit card with rates as low as 7.9% APR* and free balance transfers. Simple, straightforward card with a low rate. There is no intro APR, always a great rate.

Below is some sample content options to highlight:
$0 Annual Fee
$0 Balance Transfer Fee
No Teaser, No Intro, just a great rate

Not only could you cut your interest rate in half, but you will also save hundreds of dollars by not paying any balance transfer fees.

Apply Today! www.brivantalend.org

Target Market(s)

Ages 25-45

Industry/Entity Type

Credit Card

Requirements
Must have
• Required disclaimer: *Annual Percentage Rate. 7.9% is the preferred rate based on qualifying credit. (teeny tiny disclaimer on front of card where rate is being advertised)
• Tagline: When you need OPTIONS ... (should be placed on back of postcard by credit union name, address, and logo)

```html
<!DOCTYPE html>
<html lang="en">
<head>
<meta charset="utf-8">
<title>Springtime Saver Special Postcard</title>
<link rel="stylesheet" href="https://fonts.googleapis.com/css2?family=Roboto+Condensed:wght@300;400;700&family=Roboto:wght@400&family=Great+Vibes&family=Playfair+Display:wght@400&display=swap">
<style>
  :root {
    --page-bg: #ecebe8;
    --card-white: #ffffff;
    --top-grey: #d9dbe0;
    --blush: #f7d3de;
    --blush-light: #fdeef2;
    --magenta: #c4215c;
    --magenta-bright: #d6336f;
    --maroon: #6e1a3a;
    --ink: #1d1d1d;
    --logo-grey: #4a4a4a;
    --footer-black: #0b0b0b;
  }
  * { margin: 0; padding: 0; box-sizing: border-box; }
  html, body { width: 1200px; height: 900px; overflow: hidden; background: var(--page-bg); }
  .postcard {
    position: absolute; left: 128px; top: 85px; width: 945px; height: 730px;
    background: var(--card-white); overflow: hidden;
    box-shadow: 0 4px 18px rgba(0,0,0,.18);
  }
  .postcard__header {
    position: absolute; left: 0; top: 0; width: 100%; height: 185px;
    background: linear-gradient(180deg, var(--top-grey) 0%, #f4f4f6 60%, #ffffff 100%);
  }
  .brand {
    position: absolute; left: 62px; top: 62px;
    font-family: "Playfair Display", serif; color: var(--logo-grey); font-weight: 400;
  }
  .brand__name { font-size: 40px; line-height: 1; letter-spacing: -0.5px; }
  .brand__sub { font-size: 20px; text-align: right; margin-top: 4px; }
  .accent-stripe {
    position: absolute; left: 0; top: 181px; width: 520px; height: 14px;
    background: linear-gradient(180deg, var(--magenta) 0 45%, var(--maroon) 45% 100%);
  }
  .offer-panel {
    position: absolute; left: 0; top: 195px; width: 100%; height: 477px;
    background: linear-gradient(180deg, var(--blush) 0%, var(--blush-light) 55%, #ffffff 100%);
  }
  .headline {
    position: absolute; left: 38px; top: 222px;
    font-family: "Roboto Condensed", sans-serif; font-weight: 700; font-size: 35px;
    color: var(--ink); letter-spacing: 0.3px; white-space: nowrap;
  }
  .headline__accent { color: var(--magenta); }
  .benefit {
    position: absolute; left: 0; width: 452px;
    border-radius: 0 22px 22px 0;
    background: linear-gradient(180deg, var(--magenta-bright) 0%, var(--magenta) 40%, var(--maroon) 100%);
    color: #fff; font-family: "Roboto Condensed", sans-serif; font-weight: 700; font-size: 24px;
    line-height: 1.3; padding-left: 38px; display: flex; align-items: center;
  }
  .benefit--fee { top: 283px; height: 47px; }
  .benefit--rate { top: 359px; height: 82px; }
  .benefit--penalty { top: 478px; height: 47px; }
  .body-copy {
    position: absolute; left: 40px; top: 560px; width: 480px;
    font-family: Roboto, sans-serif; font-size: 19.5px; line-height: 1.3; color: var(--ink);
  }
  .photo-frame { position: absolute; left: 477px; top: 15px; width: 460px; height: 460px; }
  .cta {
    position: absolute; left: 555px; top: 488px; width: 330px; height: 184px;
    border-radius: 16px 16px 0 0;
    background: linear-gradient(180deg, #ee8db0 0%, var(--magenta-bright) 45%, var(--magenta) 100%);
    text-align: center;
  }
  .cta__lead {
    margin-top: 18px; font-family: "Roboto Condensed", sans-serif; font-weight: 300;
    font-size: 25px; color: var(--ink); letter-spacing: -0.3px;
  }
  .cta__strong {
    font-family: "Roboto Condensed", sans-serif; font-weight: 700; font-size: 34px;
    color: #fff; line-height: 1.05;
  }
  .cta__script { font-family: "Great Vibes", cursive; font-size: 62px; color: #fff; line-height: 1.05; }
  .postcard__footer {
    position: absolute; left: 0; top: 672px; width: 100%; height: 58px;
    background: var(--footer-black); color: #fff; text-align: center;
    font-family: Roboto, sans-serif; font-size: 22px; letter-spacing: 3px; line-height: 58px;
  }
</style>
</head>
<body>
<main class="postcard">
  <div class="postcard__header">
    <div class="brand">
      <div class="brand__name">Brivanta Community</div>
      <div class="brand__sub">credit union</div>
    </div>
  </div>
  <div class="offer-panel"></div>
  <div class="accent-stripe"></div>

  <h1 class="headline"><span class="headline__accent">SPRINGTIME SAVER</span> SPECIAL</h1>

  <div class="benefit benefit--fee">$0 Balance Transfer Fee, always</div>
  <div class="benefit benefit--rate">Always a fixed low rate,<br>as low as 7.9% APR*</div>
  <div class="benefit benefit--penalty">No penalty APR*</div>

  <p class="body-copy">Not only could you cut your interest rate in half, but you will also save hundreds of dollars by not paying any balance transfer fees - ever.</p>

  <svg class="photo-frame" viewBox="0 0 460 460" aria-hidden="false">
    <defs>
      <radialGradient id="photoTone" cx="50%" cy="45%" r="60%">
        <stop offset="0%" stop-color="#f4f1ef"/>
        <stop offset="55%" stop-color="#d9dcdc"/>
        <stop offset="100%" stop-color="#b9a6a4"/>
      </radialGradient>
    </defs>
    <circle cx="230" cy="230" r="228" fill="#c4215c"/>
    <circle cx="230" cy="230" r="219" fill="#111"/>
    <circle cx="230" cy="230" r="212" fill="url(#photoTone)" role="img" aria-label="Photo of a frosted cupcake in a pink wrapper topped with a paper heart"/>
  </svg>

  <div class="cta">
    <div class="cta__lead">WHEN YOU NEED OPTIONS</div>
    <div class="cta__strong">WE'RE HERE</div>
    <div class="cta__script">for You</div>
  </div>

  <footer class="postcard__footer">www.brivantalend.org</footer>
</main>
</body>
</html>
```